Bref créative
Business Cards, Stationery and Email signature for IT company.
Logo colors and effect are not yet selected.
I need single sided standard sized Business Card [3.5" x 2"]
Not yet selected
Simple
Olivier Brunaud
742 du Verger
Terrebonne, Québec
H2R 4K3
o.brunaud@k7v.example
www.k7v.example
The textures and effects of our logo are not yet selected. For colors, we want to have the main blue as the color. We have a preference for grey as the secondary color.
We have not made a choice at the level of the type, shape, size and position of the font/text "INFORMATIQUE D’ENTREPRISE".
When that this project is completed, there is a great possibility that we continue with the winner of this project to creates the design of our web site.
Simple k7v logo has an exemple.

```html
<!DOCTYPE html>
<html lang="fr">
<head>
<meta charset="utf-8">
<title>k7v – papeterie</title>
<link rel="stylesheet" href="https://fonts.googleapis.com/css2?family=Roboto:ital,wght@0,400;0,700;0,900;1,400&family=Dancing+Script&display=swap">
<style>
:root{
  --navy:#0c2754;
  --navy-deep:#061631;
  --blue:#1d6fd0;
  --blue-light:#5aa6f2;
  --grey-bg:#e4e5e7;
  --grey:#8a8f97;
  --grey-light:#d6d8dc;
  --paper:#ffffff;
  --ink:#333a44;
}
*{box-sizing:border-box;margin:0;padding:0}
html,body{width:1200px;height:631px;overflow:hidden}
body{background:var(--grey-bg);font-family:"Roboto",Arial,sans-serif;color:var(--ink);position:relative}
.piece{position:absolute;box-shadow:0 2px 6px rgba(0,0,0,.25);overflow:hidden}
.wordmark{font-family:"Roboto",Arial,sans-serif;font-weight:900;color:var(--paper);letter-spacing:1px;display:flex;align-items:center;gap:5px}
.wordmark .dot{display:inline-block;background:var(--blue-light);border-radius:50%}
.blue-field{background:linear-gradient(135deg,var(--navy) 0%,var(--blue) 55%,var(--navy-deep) 100%)}

/* Folder */
.folder-back{left:24px;top:12px;width:166px;height:336px;background:var(--paper)}
.folder-back .flap{position:absolute;left:0;bottom:0;width:100%;height:140px}
.folder-back .wordmark{position:absolute;left:22px;top:30px;font-size:30px}
.folder-back .wordmark.mini{top:auto;bottom:30px;left:40px;font-size:26px}
.folder-front{left:190px;top:12px;width:242px;height:336px}
.folder-front .wordmark{position:absolute;left:26px;bottom:26px;font-size:34px}
.folder-front svg{position:absolute;inset:0}
.folder-label{position:absolute;top:358px;font-size:12px;font-weight:700;color:var(--ink);letter-spacing:1px}

/* Letterhead */
.letter{left:451px;top:19px;width:228px;height:360px;background:var(--paper)}
.sheet-head{height:60px;position:relative}
.sheet-head .wordmark{position:absolute;left:12px;top:14px;font-size:24px}
.sheet-head .addr{position:absolute;right:10px;top:12px;font-size:6.5px;line-height:1.45;text-align:right;color:var(--paper)}
.letter .body{padding:14px 14px 0;font-size:6px;line-height:1.55}
.letter .body p{margin-bottom:7px}
.letter .sign{font-family:"Dancing Script",cursive;font-size:18px;color:var(--navy);margin-top:4px}

/* Fax */
.fax{left:696px;top:19px;width:235px;height:360px;background:var(--paper)}
.fax .title{position:absolute;right:14px;top:64px;font-size:24px;font-weight:900;color:var(--navy)}
.fax table{position:absolute;left:12px;top:100px;width:211px;border-collapse:collapse;font-size:6px}
.fax td{border-bottom:1px solid var(--grey-light);padding:3px 4px;height:13px}
.fax td.label{width:44px;color:var(--navy);font-weight:700}
.fax .checks{position:absolute;left:12px;top:196px;display:flex;gap:16px;font-size:6px}
.fax .checks span::before{content:"";display:inline-block;width:6px;height:6px;border:1px solid var(--grey);margin-right:3px;vertical-align:-1px}

/* Business cards */
.card{left:955px;width:221px;height:126px}
.card-front{top:19px;background:var(--paper)}
.card-front .band{position:absolute;left:0;top:0;width:86px;height:100%}
.card-front .band .wordmark{position:absolute;left:14px;top:46px;font-size:24px}
.card-front .info{position:absolute;right:10px;top:16px;text-align:right;font-size:6.5px;line-height:1.5;color:var(--ink)}
.card-front .info strong{display:block;font-size:9px;color:var(--navy);margin-bottom:4px}
.card-back{top:158px}
.card-back .wordmark{position:absolute;left:50%;top:50%;transform:translate(-50%,-50%);font-size:42px}

/* Envelope */
.envelope{left:24px;top:432px;width:408px;height:168px;background:var(--paper)}
.envelope .top{position:absolute;left:0;top:0;width:100%;height:64px}
.envelope .top .wordmark{position:absolute;left:150px;top:16px;font-size:28px}
.envelope .return{position:absolute;right:14px;top:12px;font-size:6.5px;line-height:1.45;text-align:right;color:var(--paper)}
.envelope .window{position:absolute;left:26px;top:92px;width:150px;height:50px;border:1px solid var(--grey);border-radius:3px}

/* Email window */
.mail{left:456px;top:388px;width:696px;height:232px;background:#f2f3f5;border:1px solid #a5abb4}
.mail .titlebar{height:18px;background:linear-gradient(#d9e4f3,#b8c9e2);font-size:8px;padding:4px 8px;color:#223}
.mail .menu{height:16px;font-size:7.5px;padding:3px 8px;word-spacing:8px;border-bottom:1px solid #c9ced6}
.mail .field{display:flex;align-items:center;gap:6px;padding:3px 8px;font-size:7.5px}
.mail .field .box{flex:1;height:12px;background:var(--paper);border:1px solid #b9bfc8}
.mail .compose{position:absolute;left:6px;right:6px;top:92px;bottom:6px;background:var(--paper);border:1px solid #b9bfc8;padding:8px;font-size:7px}
.mail .sig{position:absolute;left:140px;top:46px;width:300px;height:80px}
.mail .sig .wordmark{position:absolute;right:16px;top:20px;font-size:28px}
.mail .sig .addr{position:absolute;left:14px;top:14px;font-size:6.5px;line-height:1.5;color:var(--paper)}
</style>
</head>
<body>

<!-- Folder -->
<section class="piece folder-back">
  <div class="wordmark"><span class="dot" style="width:10px;height:10px"></span>k7v</div>
  <div class="flap blue-field"><div class="wordmark mini">k7v</div></div>
</section>
<section class="piece folder-front blue-field">
  <svg viewBox="0 0 242 336" width="242" height="336" aria-hidden="true">
    <path d="M0 230 C80 190 170 200 242 150 L242 336 L0 336 Z" fill="#061631" opacity=".55"/>
    <path d="M0 230 C80 190 170 200 242 150" fill="none" stroke="#5aa6f2" stroke-width="2" opacity=".7"/>
  </svg>
  <div class="wordmark">k7v</div>
</section>
<div class="folder-label" style="left:82px">« BACK</div>
<div class="folder-label" style="left:286px">FRONT »</div>

<!-- Letterhead -->
<section class="piece letter">
  <header class="sheet-head blue-field">
    <div class="wordmark"><span class="dot" style="width:8px;height:8px"></span>k7v</div>
    <div class="addr">742 du Verger<br>Terrebonne, Québec<br>H2R 4K3<br>450 555-0142<br>www.k7v.example</div>
  </header>
  <div class="body">
    <p>Le 12 mai 2024</p>
    <p>Madame, Monsieur,</p>
    <p>Nous vous remercions de votre confiance et vous présentons notre offre de services informatiques pour votre entreprise.</p>
    <p>Notre équipe assure le soutien, la sécurité et la gestion de vos réseaux au quotidien.</p>
    <p>Veuillez agréer nos salutations distinguées.</p>
    <div class="sign">Signature</div>
  </div>
</section>

<!-- Fax -->
<section class="piece fax">
  <header class="sheet-head blue-field">
    <div class="wordmark"><span class="dot" style="width:8px;height:8px"></span>k7v</div>
    <div class="addr">742 du Verger<br>Terrebonne, Québec<br>H2R 4K3<br>450 555-0142<br>www.k7v.example</div>
  </header>
  <div class="title">FAX</div>
  <table>
    <tr><td class="label">À</td><td></td></tr>
    <tr><td class="label">De</td><td></td></tr>
    <tr><td class="label">Date</td><td></td></tr>
    <tr><td class="label">Pages</td><td></td></tr>
    <tr><td class="label">Objet</td><td></td></tr>
  </table>
  <div class="checks"><span>Urgent</span><span>Pour révision</span><span>Répondre</span></div>
</section>

<!-- Business cards -->
<section class="piece card card-front">
  <div class="band blue-field"><div class="wordmark">k7v</div></div>
  <div class="info">
    <strong>Olivier Brunaud</strong>
    742 du Verger<br>Terrebonne, Québec<br>H2R 4K3<br>450 555-0142<br>o.brunaud@k7v.example<br>www.k7v.example
  </div>
</section>
<section class="piece card card-back blue-field">
  <div class="wordmark"><span class="dot" style="width:12px;height:12px"></span>k7v</div>
</section>

<!-- Envelope -->
<section class="piece envelope">
  <div class="top blue-field">
    <div class="wordmark">k7v</div>
    <div class="return">742 du Verger<br>Terrebonne, Québec<br>H2R 4K3</div>
  </div>
  <div class="window"></div>
</section>

<!-- Email signature -->
<section class="piece mail">
  <div class="titlebar">Nouveau message</div>
  <div class="menu">Fichier Édition Affichage Insertion Format Outils Message</div>
  <div class="field">À<span class="box"></span></div>
  <div class="field">Cc<span class="box"></span></div>
  <div class="field">Objet<span class="box"></span></div>
  <div class="compose">
    Bonjour, voici les documents demandés pour notre rencontre de la semaine prochaine.
    <div class="sig blue-field">
      <div class="addr">Olivier Brunaud<br>742 du Verger, Terrebonne, Québec H2R 4K3<br>450 555-0142<br>o.brunaud@k7v.example</div>
      <div class="wordmark">k7v</div>
    </div>
  </div>
</section>

</body>
</html>
```